KEV.PRO- Darren Holcombe Fitness- needs a clever business card using the logo, name, info, contact

I need a business card designed for my Online Personal Training company called KEV.PRO, abbreviation for Darren Holcombe Fitness. My company focuses on coaching in personal health and personal growth to unleash your greatest potential. I would like to see designs that use my color scheme of a redish-orange (C:0,M:84,Y:100,K:0), grey, white, black, and my company font is OSWALD. The final design should communicate some aspects of design, health, motivation, growth, in some way. The logo is very important to the company and can be displayed in any of the colors previously mentioned. Must include the company name, my website: www.kev-pro.example , my email: dan@kev-pro.example

Target Market(s)

Personal health, fitness, general public, those who lack knowledge, awareness, and confidence in personal health

Industry/Entity Type

Personal Trainer

Font styles to use
Other font styles liked:
• OSWALD. (Bold, Regular, Light)

Colors
f37122
ffffff
9d9d9d
000000

Requirements
Must have
• Must include the logo, company name, my website: www.kev-pro.example , my email: dan@kev-pro.example
Nice to have
• Variations of the colors scheme of a redish-orange (C:0,M:84,Y:100,K:0), grey, white, black. Logo, card, or text can be in any of these colors.
• Possible quote like "Take control of your personal health to unleash your greatest potential" or "Unleashing your greatness first begins with fitness of the body and mind"

```html
<!DOCTYPE html>
<html lang="en">
<head>
<meta charset="utf-8">
<title>KEV.PRO Business Card</title>
<link href="https://fonts.googleapis.com/css2?family=Oswald:wght@300;400;500;700&display=swap" rel="stylesheet">
<style>
  :root {
    --brand-orange: #f04e23;
    --ink: #111111;
    --grey: #9d9d9d;
    --paper: #ffffff;
    --backdrop: #c7b098;
  }
  * { box-sizing: border-box; margin: 0; padding: 0; }
  html, body { width: 1200px; height: 1200px; overflow: hidden; }
  body {
    background: var(--backdrop);
    font-family: "Oswald", sans-serif;
    position: relative;
  }
  .card {
    position: absolute;
    left: 180px;
    width: 840px;
    height: 480px;
    background: var(--paper);
    box-shadow: 0 10px 30px rgba(0,0,0,0.18);
    overflow: hidden;
  }
  .card--front { top: 80px; }
  .card--back { top: 640px; }

  /* Brand lockup */
  .brand {
    position: absolute;
    display: flex;
    flex-direction: column;
    align-items: center;
  }
  .brand__mark {
    width: 150px; height: 150px;
    border-radius: 50%;
    background: var(--brand-orange);
  }
  .brand__name {
    margin-top: 14px;
    font-weight: 700;
    font-size: 40px;
    line-height: 1;
    color: var(--ink);
    letter-spacing: 0.5px;
  }
  .brand__tagline {
    margin-top: 4px;
    font-weight: 300;
    font-size: 12px;
    text-transform: uppercase;
    color: var(--ink);
    letter-spacing: 0.4px;
  }
  .card--front .brand { left: 90px; top: 110px; }
  .card--back .brand { left: 50%; top: 50%; transform: translate(-50%, -50%); }
  .card--back .brand__mark { width: 170px; height: 170px; }

  /* Divider with icon column */
  .divider {
    position: absolute;
    left: 370px;
    width: 3px;
    background: var(--brand-orange);
  }
  .divider--top { top: 0; height: 150px; }
  .divider--bottom { top: 390px; height: 90px; }

  .contact-icons {
    position: absolute;
    left: 358px;
    top: 215px;
    display: flex;
    flex-direction: column;
    gap: 14px;
  }
  .contact-icon {
    width: 28px; height: 28px;
    border-radius: 50%;
    background: var(--brand-orange);
    display: flex; align-items: center; justify-content: center;
  }
  .contact-icon svg { width: 16px; height: 16px; }

  /* Person and details */
  .person {
    position: absolute;
    left: 410px;
    top: 145px;
  }
  .person__name {
    font-weight: 400;
    font-size: 36px;
    line-height: 1;
    color: var(--brand-orange);
    text-transform: uppercase;
  }
  .person__role {
    font-weight: 400;
    font-size: 18px;
    color: var(--ink);
    text-transform: uppercase;
    margin-top: 2px;
  }
  .details {
    position: absolute;
    left: 410px;
    top: 215px;
    list-style: none;
    display: flex;
    flex-direction: column;
    gap: 14px;
  }
  .details li {
    height: 28px;
    line-height: 28px;
    font-size: 21px;
    font-weight: 400;
    color: var(--ink);
  }
</style>
</head>
<body>

<section class="card card--front" aria-label="Business card front">
  <div class="brand">
    <div class="brand__mark"></div>
    <div class="brand__name">KEV.PRO</div>
    <div class="brand__tagline">Darren Holcombe Fitness</div>
  </div>

  <div class="divider divider--top"></div>
  <div class="divider divider--bottom"></div>

  <div class="person">
    <h1 class="person__name">Alex Carter</h1>
    <p class="person__role">Designation</p>
  </div>

  <div class="contact-icons">
    <span class="contact-icon">
      <svg viewBox="0 0 16 16"><path d="M4 2 L6.5 2 L7.5 5 L6 6.3 C6.8 8 8 9.2 9.7 10 L11 8.5 L14 9.5 L14 12 C14 13 13 14 12 14 C7 13.5 2.5 9 2 4 C2 3 3 2 4 2 Z" fill="#fff"/></svg>
    </span>
    <span class="contact-icon">
      <svg viewBox="0 0 16 16"><rect x="2" y="4" width="12" height="8" rx="1" fill="#fff"/><path d="M2.5 4.5 L8 9 L13.5 4.5" stroke="#f04e23" stroke-width="1.2" fill="none"/></svg>
    </span>
    <span class="contact-icon">
      <svg viewBox="0 0 16 16"><path d="M8 1.5 C5.2 1.5 3.5 3.5 3.5 6 C3.5 9.5 8 14.5 8 14.5 C8 14.5 12.5 9.5 12.5 6 C12.5 3.5 10.8 1.5 8 1.5 Z" fill="#fff"/><circle cx="8" cy="6" r="1.8" fill="#f04e23"/></svg>
    </span>
    <span class="contact-icon">
      <svg viewBox="0 0 16 16" fill="none" stroke="#fff" stroke-width="1.3"><circle cx="8" cy="8" r="6"/><ellipse cx="8" cy="8" rx="2.6" ry="6"/><path d="M2 8 H14"/></svg>
    </span>
  </div>

  <ul class="details">
    <li>010 555 0199</li>
    <li>dan@kev-pro.example</li>
    <li>12 Harbor Ln. Kailua, HI 96734</li>
    <li>www.kev-pro.example</li>
  </ul>
</section>

<section class="card card--back" aria-label="Business card back">
  <div class="brand">
    <div class="brand__mark"></div>
    <div class="brand__name">KEV.PRO</div>
    <div class="brand__tagline">Darren Holcombe Fitness</div>
  </div>
</section>

</body>
</html>
```